The Copper Hour ebook cover for Desmond Okafor Whitley

I need an ebook cover/jpeg that depicts a Middle-Eastern desert and sky. The cover must be very elegant and very austere, the simpler the better.
Toward the top, the text will read: The Copper Hour
Directly below the title will read: Corvin Teague
The dimensions for the cover should be 2560 pixels (height) and 1600 pixels (width.)

Target Market(s)

Readers of serious magical realism and/or fantasy literature with a serious literary element.

Font styles to use
Serif

Requirements
Must have
• My ebook cover MUST be a painting or illustration depicting a very austere Middle-Eastern desert and desert sky. Must be elegant and austere. The lettering of the title and author name must blend in beautifully with the image--just like fine books in a bookstore. Title must appear at the top: The Copper Hour. The author's name must appear below title and read: Corvin Teague. Dimensions must be 2560 pixels (height) by 1600 pixels (width)
Nice to have
• A very austere desert on the bottom and a sad elegant sky above.
Should not have
• My ebook cover should not have a spine or a back. I just need an ebook cover of the dimensions stated above.

```html
<!DOCTYPE html>
<html lang="en">
<head>
<meta charset="utf-8">
<title>The Copper Hour — Corvin Teague</title>
<link rel="stylesheet" href="https://fonts.googleapis.com/css2?family=Aladin&family=Bodoni+Moda:wght@400;500&display=swap">
<style>
  :root {
    --sky-top: #070f22;
    --sky-mid: #0f1f42;
    --sky-low: #1d3263;
    --dune-shadow: #1c2640;
    --dune-lit: #d9c893;
    --sand-near: #4a4438;
    --sand-deep: #0d0b08;
    --gold-light: #fbf4d2;
    --gold-mid: #e2cf92;
    --gold-deep: #b0904c;
  }
  * { margin: 0; padding: 0; box-sizing: border-box; }
  html, body {
    width: 750px;
    height: 1200px;
    overflow: hidden;
    background: var(--sky-top);
  }
  .cover {
    position: relative;
    width: 750px;
    height: 1200px;
    overflow: hidden;
  }
  .cover__scene {
    position: absolute;
    inset: 0;
    background: linear-gradient(
      to bottom,
      var(--sky-top) 0%,
      var(--sky-mid) 40%,
      var(--sky-low) 62%,
      var(--dune-shadow) 66%,
      var(--dune-lit) 80%,
      var(--sand-near) 86%,
      #2a2620 93%,
      var(--sand-deep) 100%
    );
  }
  .cover__titles {
    position: absolute;
    top: 150px;
    left: 0;
    width: 100%;
    text-align: center;
  }
  .gilded {
    background: linear-gradient(to bottom, var(--gold-light) 0%, var(--gold-mid) 55%, var(--gold-deep) 100%);
    -webkit-background-clip: text;
    background-clip: text;
    color: transparent;
  }
  .title__article {
    display: block;
    font-family: "Aladin", cursive;
    font-size: 52px;
    line-height: 1;
  }
  .title__line {
    display: block;
    font-family: "Bodoni Moda", serif;
    font-weight: 400;
    line-height: 1;
  }
  .title__line--upper {
    font-size: 104px;
    margin-top: 8px;
    letter-spacing: 1px;
  }
  .title__line--lower {
    font-size: 176px;
    margin-top: -6px;
    letter-spacing: 2px;
  }
  .author {
    display: block;
    margin-top: 10px;
    font-family: "Aladin", cursive;
    font-size: 52px;
    line-height: 1.1;
    letter-spacing: 1px;
  }
</style>
</head>
<body>
  <main class="cover">
    <div class="cover__scene" role="img" aria-label="Night desert photograph: starry deep blue sky above moonlit sand dunes with sparse grass tufts and rippled sand in the foreground"></div>
    <header class="cover__titles">
      <h1>
        <span class="title__article gilded">The</span>
        <span class="title__line title__line--upper gilded">COPPER</span>
        <span class="title__line title__line--lower gilded">HOUR</span>
      </h1>
      <p class="author gilded">Corvin Teague</p>
    </header>
  </main>
</body>
</html>
```